Health care product retail website

We need a website design for a company based in New Zealand that sells fresh air to an overseas market.
There are 4 products to start with and we have a logo. We need to give the message that it is unpolluted and clean. We are also promoting a self-sustaining business model by investing in the planet's future. The website will be developed in WordPress and if you can suggest coding thats a bonus, but not necessary as I can develop in Wordpress.

Target Market(s)

Chinese, Indian, Middle Eastern or anywhere where the air is quite polluted. middle-income target market

Industry/Entity Type

Health And Wellness

Number of Pages Required

5+ page

Font styles to use
Sans Serif

Requirements
Must have
• Homepage: Clean, fresh look. Indicate that the product is sourced and bottled in a clean environment.
• Any help with e-commerce and multilingual pages appreciated.
• Home, Products, Our locations, Environmental protection, Science

```html
<!DOCTYPE html>
<html lang="en">
<head>
<meta charset="utf-8">
<title>Aroha Air – Home</title>
<link href="https://fonts.googleapis.com/css2?family=Lato:wght@400;700;900&display=swap" rel="stylesheet">
<style>
:root{
  --green:#8dc63f;
  --green-dark:#6fa82a;
  --blue:#29a3e0;
  --ink:#2b2b2b;
  --text:#555;
  --topbar:#ececec;
  --soft:#f3f4f6;
  --forest:#1d2418;
  --footer:#2f2f35;
  --footer-deep:#1f1f23;
}
*{box-sizing:border-box;margin:0;padding:0}
html,body{width:800px;height:1200px;overflow:hidden}
body{font-family:'Lato',sans-serif;color:var(--text);background:#fff;position:relative}
.wrap{width:586px;margin:0 auto;position:relative}

.topbar{height:26px;background:var(--topbar);border-bottom:1px solid #ddd}
.topbar .wrap{display:flex;justify-content:flex-end;height:100%}
.social-top{display:flex}
.social-top span{width:24px;height:26px;border-left:1px solid #d6d6d6;display:flex;align-items:center;justify-content:center}
.social-top span i{width:8px;height:8px;background:#a9a9a9;display:block}
.lang{border-left:1px solid #d6d6d6;padding:0 8px;display:flex;align-items:center;gap:5px;font-size:8px;color:#333;width:74px}
.lang .dot{width:10px;height:10px;border-radius:50%;background:#4a5c9a}

.header{height:68px;background:linear-gradient(#fff,#f4f4f4)}
.header .wrap{display:flex;align-items:center;height:100%}
.brand{font-weight:900;font-size:26px;color:var(--green)}
.header-info{margin-left:auto;display:flex;gap:16px;align-items:center}
.info{display:flex;align-items:center;gap:6px;font-size:7.5px;color:#555;line-height:1.4}
.info b{display:block;font-size:9px;color:#222;font-weight:700}

.nav{height:27px;background:var(--green)}
.nav .wrap{display:flex;align-items:center;height:100%}
.nav a{color:#fff;text-decoration:none;font-size:8.5px;padding:0 11px;height:27px;line-height:27px}
.nav a.active{background:var(--green-dark)}
.search{margin-left:auto;width:116px;height:18px;border-radius:9px;background:rgba(0,0,0,.12);display:flex;align-items:center;justify-content:space-between;padding:0 9px;font-size:7px;color:#eaf5da}

.hero{height:247px;background:radial-gradient(ellipse at 75% 20%,#e6f2a0 0%,#9fbf3e 30%,#5f8a2a 60%,#3e5e22 100%);display:flex;align-items:center;justify-content:center}
.hero-title{text-align:center;color:#fff;font-weight:900;font-size:17px;line-height:1.25;padding:8px 30px;border-top:1px solid rgba(0,0,0,.5);border-bottom:1px solid rgba(0,0,0,.5);text-shadow:0 1px 3px rgba(0,0,0,.4);margin-top:18px}

.about{height:180px;text-align:center;padding-top:52px}
.section-title{font-size:22px;font-weight:900;color:var(--ink)}
.section-title span{color:var(--green)}
.about p{width:576px;margin:14px auto 0;font-size:7.4px;line-height:1.75;color:#555}

.products{height:340px;background:var(--soft);padding-top:52px;text-align:center}
.grid{display:flex;justify-content:space-between;margin-top:30px}
.card{width:136px;height:185px;background:#fff;border:1px solid #e6e6e6;position:relative}
.card.hover{background:#c8ecf2}
.card .photo{width:40px;height:115px;margin:12px auto 0;border-radius:12px 12px 6px 6px}
.photo.clear{background:linear-gradient(90deg,#9fc7d0,#d8eef2,#8fb8c3)}
.photo.dark{background:linear-gradient(90deg,#111,#444,#111)}
.photo.pair{width:70px}
.card h3{font-size:8px;font-weight:700;color:#333;margin-top:22px}
.card .rule{width:40px;height:2px;background:var(--green);margin:5px auto}
.card.hover .rule{background:var(--blue)}
.card .price{font-size:10.5px;font-weight:700;color:#222}
.quick{position:absolute;left:7px;top:102px;width:120px;height:24px;background:#fff;display:flex;font-size:7px;color:var(--green)}
.quick span{border-right:1px solid #eee;width:24px;display:flex;align-items:center;justify-content:center}
.quick span:last-child{border:0;flex:1;gap:4px}

.promo{height:82px;background:linear-gradient(90deg,#141a12,#2a3424,#141a12)}
.promo .wrap{display:flex;align-items:center;justify-content:space-between;height:100%}
.promo h2{color:#fff;font-size:17px;font-weight:700}
.btn{border:1px solid #fff;color:#fff;font-size:7.5px;font-weight:700;padding:7px 12px}

.contact-band{height:52px;background:var(--green);color:#fff}
.contact-band .wrap{display:flex;align-items:center;height:100%;font-size:7.5px;line-height:1.45}
.contact-band b{font-weight:700}
.cb-item{display:flex;align-items:center;gap:8px}
.cb-social{margin-left:auto;display:flex;gap:5px}
.cb-social i{width:18px;height:18px;background:var(--green-dark);display:block}

.footer{height:148px;background:var(--footer);color:#ddd}
.footer .wrap{display:flex;padding-top:27px}
.col h4{font-size:11px;font-weight:400;color:#fff;text-transform:uppercase}
.col .bar{width:24px;height:2px;background:var(--blue);margin:6px 0 14px}
.col p{font-size:6.6px;line-height:1.45}
.col.t{width:206px}.col.n{width:205px}.col.s{flex:1}
.author{display:flex;align-items:center;gap:10px;margin-top:7px}
.avatar{width:28px;height:28px;border-radius:50%;background:#c9a58a}
.author b{font-size:7px;font-weight:400;color:#fff;display:block}
.author small{font-size:6.5px;color:#777}
.links{display:grid;grid-template-columns:78px 80px;row-gap:13px;font-size:7px;font-weight:700}
.links span::before{content:"";display:inline-block;width:4px;height:4px;border:1px solid #ddd;border-radius:50%;margin-right:4px}
.email{margin-top:12px;height:26px;background:#3c3c43;display:flex;align-items:center;justify-content:space-between;padding:0 8px;font-size:7px;color:#999}

.copyright{height:30px;background:var(--footer-deep);color:#ccc;font-size:7.5px;text-align:center;line-height:30px}
</style>
</head>
<body>

<div class="topbar"><div class="wrap">
  <div class="social-top"><span><i></i></span><span><i></i></span><span><i></i></span></div>
  <div class="lang"><span class="dot"></span>English ▾</div>
</div></div>

<header class="header"><div class="wrap">
  <div class="brand">Aroha Air</div>
  <div class="header-info">
    <div class="info">
      <svg width="20" height="20" viewBox="0 0 20 20"><circle cx="10" cy="10" r="9" fill="none" stroke="#29a3e0" stroke-width="2"/><path d="M7 6l2 2-1 2 2 2 2-1 2 2-2 2c-4 0-8-4-8-8z" fill="#29a3e0"/></svg>
      <div><b>Call Us:</b>(555) 301 42 18 / 30 57 66</div>
    </div>
    <div class="info">
      <svg width="24" height="22" viewBox="0 0 24 22"><path d="M1 3h4l3 11h11l3-8H7" fill="none" stroke="#29a3e0" stroke-width="2.4"/><circle cx="10" cy="18" r="2" fill="#29a3e0"/><circle cx="18" cy="18" r="2" fill="#29a3e0"/></svg>
      <div><b>Shopping Cart</b>0 items ▾</div>
    </div>
  </div>
</div></header>

<nav class="nav"><div class="wrap">
  <a class="active">Home</a><a>Products</a><a>Our locations</a><a>Environmental protection</a><a>Science</a><a>Contact Us</a>
  <div class="search">Search <svg width="8" height="8" viewBox="0 0 8 8"><circle cx="3.3" cy="3.3" r="2.4" fill="none" stroke="#fff" stroke-width="1.2"/><path d="M5 5l2.5 2.5" stroke="#fff" stroke-width="1.2"/></svg></div>
</div></nav>

<section class="hero" role="img" aria-label="Misty green forest with moss-covered stones and sunbeams">
  <h1 class="hero-title">Enhancing Stamina In One Breath<br>At A Time</h1>
</section>

<section class="about">
  <h2 class="section-title">About <span>Aroha Air</span></h2>
  <p>Lorem Ipsum Dolor Sit Amet, Consectetur Adipiscing Elit, Sed Do Eiusmod Tempor Incididunt Ut Labore Et Dolore Magna Aliqua. Ut Enim Ad Minim Veniam, Quis Nostrud Exercitation Ullamco Laboris Nisi Ut Aliquip Ex Ea Commodo Consequat. Duis Aute Irure Dolor In Reprehenderit In Voluptate Velit Esse Cillum Dolore Eu Fugiat Nulla Pariatur. Excepteur Sint Occaecat Cupidatat Non Proident, Sunt In Culpa Qui Officia Deserunt Mollit Anim Id Est Laborum. Sed Ut Perspiciatis Unde Omnis Iste Natus Error Sit Voluptatem Accusantium Doloremque Laudantium, Totam Rem Aperiam, Eaque Ipsa Quae Ab Illo Inventore Veritatis Et Quasi Architecto Beatae Vitae Dicta Sunt Explicabo.</p>
</section>

<section class="products"><div class="wrap">
  <h2 class="section-title">Our <span>Products</span></h2>
  <div class="grid">
    <div class="card hover">
      <div class="photo clear pair" role="img" aria-label="Two clear air canisters"></div>
      <div class="quick"><span>🛒</span><span>♡</span><span>⊕ QUICK VIEW</span></div>
      <h3>Summit Air 3</h3><div class="rule"></div><div class="price">$13.49</div>
    </div>
    <div class="card">
      <div class="photo dark" role="img" aria-label="Black air cylinder with valve"></div>
      <h3>Summit Air 3</h3><div class="rule"></div><div class="price">$13.49</div>
    </div>
    <div class="card">
      <div class="photo clear" role="img" aria-label="Clear air canister"></div>
      <h3>Summit Air 3</h3><div class="rule"></div><div class="price">$13.49</div>
    </div>
    <div class="card">
      <div class="photo dark" role="img" aria-label="Dark air cylinder with brass valve"></div>
      <h3>Summit Air 1</h3><div class="rule"></div><div class="price">$13.49</div>
    </div>
  </div>
</div></section>

<section class="promo" role="img" aria-label="Dark forest background"><div class="wrap">
  <h2>IT IS UNPOLLUTED AND CLEAN.</h2>
  <span class="btn">CONTACT US</span>
</div></section>

<section class="contact-band"><div class="wrap">
  <div class="cb-item" style="width:297px">
    <svg width="9" height="12" viewBox="0 0 9 12"><path d="M4.5 0a4.5 4.5 0 0 1 4.5 4.5C9 8 4.5 12 4.5 12S0 8 0 4.5A4.5 4.5 0 0 1 4.5 0z" fill="#fff"/><circle cx="4.5" cy="4.5" r="1.6" fill="#8dc63f"/></svg>
    <div><b>Aroha Air Ltd</b><br>123, Lorem Ipsum Dolor Sit Amet, Consectetur</div>
  </div>
  <div class="cb-item">
    <svg width="14" height="12" viewBox="0 0 14 12"><path d="M1 3l4 4-1 2 3 2 3-3" fill="none" stroke="#fff" stroke-width="1.6"/></svg>
    <div>(555) 480 - 219 - 3364<br>hello@arohaair.example</div>
  </div>
  <div class="cb-social"><i></i><i></i><i></i></div>
</div></section>

<footer class="footer"><div class="wrap">
  <div class="col t">
    <h4>Testimonials</h4><div class="bar"></div>
    <p>But I must explain to you how all this<br>mistaken idea of denouncing pleasure and<br>praising pain was born and I wil</p>
    <div class="author"><div class="avatar" role="img" aria-label="Customer portrait"></div><div><b>Mara</b><small>Lorem ipsum</small></div></div>
  </div>
  <div class="col n">
    <h4>Navigation</h4><div class="bar"></div>
    <div class="links"><span>Home</span><span>Science</span><span>Products</span><span>Contact Us</span><span>Our locations</span></div>
  </div>
  <div class="col s">
    <h4>Newsletter Signup</h4><div class="bar"></div>
    <p>Lorem ipsum dolor sit amet, consectetur<br>adipiscing elit, sed do eiusmod tempor incididunt</p>
    <div class="email">Enter email address <span style="color:#fff">›</span></div>
  </div>
</div></footer>

<div class="copyright">© 2016 AROHA AIR. ALL RIGHTS RESERVED.</div>

</body>
</html>
```